Crimson Lantern Harbor, Topics; Nursing, Military, Family and Faith

Three word Title with topics underlined beneath.
It will be a book cover on which I would like to capture a Vision of each topic if possible.

It is a 9"x 6" single book blending the 4 topics throughout the text.
I had a the title and topics framed in the middle, with pics of nature above and below but would like something different that catches the eye relating more to the text.

Target Market(s)

Nurses, patients and family, Non-Christians / Christians, and Military.

Font styles to use
Script

Colors

Requirements
Must have
• Title underlined by topics, over illustrated background
Nice to have
• If possible, use topics for background behind the title.

```html
<!DOCTYPE html>
<html lang="en">
<head>
<meta charset="utf-8">
<title>Crimson Lantern Harbor — Book Cover</title>
<link rel="stylesheet" href="https://fonts.googleapis.com/css2?family=Dancing+Script:wght@700&family=Archivo:wght@800&display=swap">
<style>
  :root {
    --page-bg: #e9eaec;
    --cover-deep: #0b1a4a;
    --cover-mid: #1f4fa8;
    --cover-teal: #2fb6c8;
    --cover-green: #1d4a3e;
    --panel: rgba(6, 14, 22, 0.82);
    --frame-fill: #0d171c;
    --frame-line: #9fb4c4;
    --gold-light: #fff4d6;
    --gold: #e8c98a;
    --gold-deep: #b88a3e;
    --topic-text: #ffffff;
  }
  * { margin: 0; padding: 0; box-sizing: border-box; }
  html, body {
    width: 1200px;
    height: 1200px;
    overflow: hidden;
    background: var(--page-bg);
  }
  .book-cover {
    position: absolute;
    left: 232px;
    top: 50px;
    width: 735px;
    height: 1100px;
    overflow: hidden;
    background: var(--cover-deep);
  }
  .cover-art {
    position: absolute;
    inset: 0;
    background:
      radial-gradient(ellipse at 75% 30%, rgba(47,182,200,0.75) 0%, rgba(47,182,200,0) 55%),
      radial-gradient(ellipse at 15% 75%, rgba(29,74,62,0.8) 0%, rgba(29,74,62,0) 50%),
      linear-gradient(170deg, var(--cover-mid) 0%, var(--cover-deep) 55%, #081238 100%);
  }
  .title-panel {
    position: absolute;
    left: 129px;
    top: 312px;
    width: 484px;
    height: 577px;
    background: var(--panel);
  }
  .title-frame {
    position: absolute;
    left: 166px;
    top: 351px;
    width: 406px;
    height: 401px;
    border: 3px solid var(--frame-line);
    padding: 9px;
  }
  .title-frame-inner {
    width: 100%;
    height: 100%;
    background: var(--frame-fill);
  }
  .book-title {
    position: absolute;
    left: 166px;
    top: 351px;
    width: 406px;
    height: 401px;
    display: flex;
    flex-direction: column;
    justify-content: center;
    align-items: center;
    font-family: "Dancing Script", cursive;
    font-weight: 700;
    font-size: 80px;
    line-height: 106px;
    text-align: center;
    background: linear-gradient(180deg, var(--gold-light) 0%, var(--gold) 60%, var(--gold-deep) 100%);
    -webkit-background-clip: text;
    background-clip: text;
    color: transparent;
    filter: drop-shadow(2px 3px 2px rgba(0,0,0,0.7));
  }
  .book-title span { display: block; }
  .title-glow {
    position: absolute;
    left: 240px;
    top: 743px;
    width: 250px;
    height: 6px;
    border-radius: 50%;
    background: radial-gradient(ellipse at center, #fff3c8 0%, #f0a640 45%, rgba(240,166,64,0) 100%);
  }
  .topics {
    position: absolute;
    left: 129px;
    top: 806px;
    width: 484px;
    text-align: center;
    font-family: "Archivo", sans-serif;
    font-weight: 800;
    font-size: 20px;
    letter-spacing: 0.5px;
    color: var(--topic-text);
  }
  .topics .divider { margin: 0 5px; }
</style>
</head>
<body>
  <main class="book-cover">
    <div class="cover-art" role="img" aria-label="Photo of a uniformed service member walking toward his waiting family at a home entrance, overlaid with translucent blue and teal geometric light shards"></div>
    <div class="title-panel"></div>
    <div class="title-frame"><div class="title-frame-inner"></div></div>
    <h1 class="book-title"><span>Crimson</span><span>Lantern</span><span>Harbor</span></h1>
    <div class="title-glow"></div>
    <p class="topics">NURSING<span class="divider">|</span>MILITARY<span class="divider">|</span>FAMILY<span class="divider">|</span>FAITH</p>
  </main>
</body>
</html>
```